Update cover page from corporate ppt template

We would like you to design a new cover page for our corporate presentation template

Attached you will find our existing template with the previous cover pages used in the past years.

As you can see, we have used transparency lines in different directions and also tried to develop a new design with mosaic/squares but we are not entirely satisfied (logo lost in the sky, ...)

You can reuse the same picture (mountain with the bridge, i.e not the one of the last cover page)

Feel free to come up with new ideas

```html
<!DOCTYPE html>
<html lang="en">
<head>
<meta charset="utf-8">
<title>Board of Directors – Cover</title>
<link href="https://fonts.googleapis.com/css2?family=Arimo:wght@400&family=Tinos:wght@400&display=swap" rel="stylesheet">
<style>
  :root {
    --canvas-bg: #e9eaec;
    --slide-white: #ffffff;
    --title-blue: #7690c6;
    --brand-grey: #7d7d7f;
    --sky-pale: #dceaf3;
    --sky-mid: #a9cbe0;
    --peak-blue: #6d88a6;
    --meadow-green: #6f8a3a;
    --meadow-gold: #c59a3c;
    --lake-blue: #3f86bb;
    --lake-deep: #1f5f93;
  }
  * { margin: 0; padding: 0; box-sizing: border-box; }
  html, body {
    width: 1200px;
    height: 1200px;
    overflow: hidden;
    background: var(--canvas-bg);
  }
  .cover-slide {
    position: absolute;
    left: 112px;
    top: 206px;
    width: 974px;
    height: 730px;
    background: var(--slide-white);
    overflow: hidden;
  }
  .cover-photo {
    position: absolute;
    inset: 0;
    background:
      linear-gradient(90deg, rgba(111,138,58,0.25) 0%, rgba(0,0,0,0) 45%, rgba(197,154,60,0.35) 100%),
      linear-gradient(180deg,
        var(--slide-white) 0%,
        var(--slide-white) 22%,
        var(--sky-pale) 32%,
        var(--sky-mid) 40%,
        #c9d6e2 48%,
        var(--peak-blue) 56%,
        var(--meadow-green) 63%,
        var(--meadow-gold) 68%,
        var(--lake-blue) 75%,
        #5c95bf 82%,
        var(--lake-deep) 100%);
  }
  .brand-name {
    position: absolute;
    left: 68px;
    top: 72px;
    font-family: "Tinos", serif;
    font-weight: 400;
    font-size: 46px;
    letter-spacing: 1px;
    color: var(--brand-grey);
  }
  .cover-heading {
    position: absolute;
    right: 85px;
    top: 66px;
    text-align: right;
    font-family: "Arimo", Arial, sans-serif;
    font-weight: 400;
    color: var(--title-blue);
  }
  .cover-title {
    font-size: 34px;
    line-height: 40px;
  }
  .cover-date {
    font-size: 24px;
    line-height: 32px;
    margin-top: 2px;
  }
</style>
</head>
<body>
  <section class="cover-slide">
    <div class="cover-photo" role="img" aria-label="Photograph of a person walking along a rope suspension bridge across a calm alpine lake, with green and golden hills and snow-capped mountains reflected in the water"></div>
    <div class="brand-name">VERANTO</div>
    <div class="cover-heading">
      <h1 class="cover-title" style="font-weight:400">Board of Directors</h1>
      <p class="cover-date">May 2024</p>
    </div>
  </section>
</body>
</html>
```